Business card needed for home based pen making business.

I'm after a business card that's a bit more than an off the shelf card. I do like the idea of a card split horizontal with different colours used. A third colour is to be used for the business name and if need a forth for the other details.

I don't have a logo and will pay extra for one ($150 extra). I mainly make pens and seam rippers (stitch unpicks). The logo may be used for a website in future, as will the colours so please provide the colour codes and font type.

I'd like the business name in an easy to read script font at the top (with logo if you have one) and the other details to the bottom left hand side. I'll leave it up to you to match the script to the font used for the other details.

I'd like to keep a triangular balance to the card so something like a siloet of pot containing pens on the bottom right could be used to balance it out. There my ideas I want to see your.

Business name: Quill & Co
Email address: quillandco@mailbox-example.net
Contact: Trevor
Phone: 0412 555 874
No address is to be used on card.

Target Market(s)

Wide variety of people visiting craft markets. Age range 30+.

Industry/Entity Type

Business

Contact Information for Business Card

Quill & Co

Font styles to use
Script

Colors
f0ecf4
3277b5
3176b5

Requirements
Must have
• Contact: Trevor
• Phone: 0412 555 874
• Email address: quillandco@mailbox-example.net
Nice to have
• An icon and/or graphics depicting pens and seam rippers..
Should not have
• I don't want icon/ graphic to be a crossed pen and seam ripper.

```html
<!DOCTYPE html>
<html lang="en">
<head>
<meta charset="utf-8">
<title>Quill &amp; Co — Business Card</title>
<link rel="stylesheet" href="https://fonts.googleapis.com/css2?family=Jost:wght@400&family=Kaushan+Script&display=swap">
<style>
  :root {
    --page: #ffffff;
    --card: #fcf8e1;
    --ink-brown: #7a3f12;
    --band-1: #0396d3;
    --band-2: #03a6cf;
    --band-3: #0279a8;
    --band-4: #026d92;
    --nib: #036f98;
  }
  * { margin: 0; padding: 0; box-sizing: border-box; }
  html, body {
    width: 1200px;
    height: 1200px;
    overflow: hidden;
    background: var(--page);
  }
  .card {
    position: absolute;
    left: 346px;
    top: 192px;
    width: 486px;
    height: 802px;
    background: var(--card);
    overflow: hidden;
  }
  .card__bands {
    position: absolute;
    inset: 0;
    width: 100%;
    height: 100%;
  }
  .band--1 { fill: var(--band-1); }
  .band--2 { fill: var(--band-2); }
  .band--3 { fill: var(--band-3); }
  .band--4 { fill: var(--band-4); }
  .nib-artwork { fill: var(--nib); }
  .business-name {
    position: absolute;
    left: 178px;
    top: 122px;
    width: 290px;
    text-align: center;
    font-family: "Kaushan Script", cursive;
    font-weight: 400;
    font-size: 112px;
    line-height: 108px;
    color: var(--ink-brown);
  }
  .business-name span { display: block; }
  .contact {
    position: absolute;
    left: 246px;
    top: 670px;
    width: 200px;
    text-align: center;
    font-family: "Jost", sans-serif;
    font-weight: 400;
    font-size: 21px;
    line-height: 32px;
    color: var(--ink-brown);
    letter-spacing: 0.3px;
  }
  .contact__email { white-space: nowrap; font-size: 17px; margin-left: -40px; margin-right: -40px; }
</style>
</head>
<body>
  <div class="card">
    <svg class="card__bands" viewBox="0 0 608 1003" preserveAspectRatio="none" aria-hidden="false">
      <rect class="band band--1" x="41" y="0" width="44" height="1003"/>
      <rect class="band band--2" x="85" y="0" width="44" height="790"/>
      <rect class="band band--3" x="129" y="0" width="44" height="632"/>
      <rect class="band band--4" x="173" y="0" width="43" height="632"/>
      <rect class="nib-artwork" x="133" y="632" width="125" height="371" role="img" aria-label="Silhouette of a fountain pen nib continuing the blue bands"/>
    </svg>

    <h1 class="business-name"><span>Quill</span><span>&amp;</span><span>Co</span></h1>

    <div class="contact">
      <p class="contact__email">quillandco@mailbox-example.net</p>
      <p class="contact__name">Trevor</p>
      <p class="contact__phone">0412 555 874</p>
    </div>
  </div>
</body>
</html>
```